Wall Sticker (3 design options)

We need 3 design options for wall sticker design, taking inspiration from the Roll-Up Banner PDF files. The wall sticker will promote our school's courses and qualifications.

Size of wall sticker: 2400 mm (height) x 900 mm (width)

Wall sticker will be installed next to our classroom entrance (refer to photo of wall - file name: BRMVA Wall & Glass Panel Size.jpg

Background on our business (for your own knowledge): Our company is called Weaving and Apparel Learning Institute (BrM.va). We help train the fashion industry as well as people who are interested in joining the fashion industry.

Must Have:
- Take colour scheme from uploaded PDF files
- Hex code for corporate colour is #DA291C (Red)
- Other Corporate Colours to be Included: Grey, White, Black

Font Type to be used: Frutiger

Logos to be used are attached: BrM.va logo, KPH LNR logo, and LearnSeal logo

=======================================================
This is the text content for the wall sticker:

STEP INTO THE WORLD OF FASHION

PROFESSIONAL KPH SHORT COURSES
- Fashion Styling
- Sewing and Alteration
- Leather Care
- Fabric Care

KPH ADVANCED CERTIFICATE IN FASHION TECHNOLOGY
• Apparel Design and Product Development
• Merchandising and Marketing

KPH DIPLOMA IN FASHION TECHNOLOGY:
• Footwear Design and Product Development

FUNDING & CAREER OPPORTUNITIES
Speak to us today about your eligibility in funding and potential career opportunities upon graduation.

Tel: 38249057
Email: enquiry@brmva-example.org
Website: www.brmva-example.edu.sg

Stock photo: please propose stock photos for the 3 design options. The photo should 'speak' about fashion in general but not specifically on sewing, footwear making, etc but should be generic. Please do not use runway photos or photos that have fashion illustrations.

FINAL ARTWORK requirements:
- Source file format: saved for Adobe Illustrator CS6 (ai), not locked so that we can make edits in future
- Print file format: PDF (editable and not locked), must include crop marks and 3 mm bleed.

Target Market(s)

General Public, Fashionistas, Fashion Students, Aspiring Footwear Enthusiasts and people interested to enter the fashion industry

Font styles to use
Sans Serif
Other font styles liked:
• Frutiger

Colors
ec1f27
ffffff
000000
757575
c5c5c5

Requirements
Must have
• - Hex code for corporate colour is #DA291C (Red)
• - Other Corporate Colours to be Included: Grey, White, Black
• Please put in the header (at the top): BrM.va logo
• Please put somewhere in the footer (bottom):
• - KPH LNR logo
• - LearnSeal logo
• - our contact details and website - telephone: 38249057, email: enquiry@brmva-example.org, and website: www.brmva-example.edu.sg
Should not have
• stock photo with fashion illustration

```html
<!DOCTYPE html>
<html lang="en">
<head>
<meta charset="utf-8">
<title>BrM.va – Step Into the World of Fashion</title>
<link rel="stylesheet" href="https://fonts.googleapis.com/css2?family=Noto+Sans:ital,wght@0,400;0,600;0,700;0,800;1,800;1,900&display=swap">
<style>
  :root {
    --red: #da291c;
    --black: #000000;
    --charcoal: #141414;
    --stripe: #262626;
    --grey: #c5c5c5;
    --grey-dark: #757575;
    --white: #ffffff;
    --ink: #1a1a1a;
  }
  * { margin: 0; padding: 0; box-sizing: border-box; }
  html, body { width: 1200px; height: 3197px; overflow: hidden; background: var(--white); }
  body { font-family: "Noto Sans", Arial, sans-serif; color: var(--ink); }

  .sticker { position: relative; width: 1200px; height: 3197px; overflow: hidden; background: var(--white); }
  .layer { position: absolute; inset: 0; width: 1200px; height: 3197px; }

  /* bands */
  .band-top { background: var(--black); clip-path: polygon(0 150px, 1200px 150px, 1200px 560px, 0 670px); }
  .stripe-a { background: var(--stripe); clip-path: polygon(0 230px, 1200px 420px, 1200px 470px, 0 300px); }
  .stripe-b { background: var(--charcoal); clip-path: polygon(0 470px, 1200px 180px, 1200px 240px, 0 540px); }
  .stripe-red { background: var(--red); clip-path: polygon(700px 620px, 1200px 555px, 1200px 600px, 700px 650px); }

  .band-grey-1 { background: var(--grey); clip-path: polygon(0 940px, 1200px 1000px, 1200px 1130px, 0 1210px); }
  .band-grey-2 { background: var(--grey); clip-path: polygon(0 1600px, 1200px 1560px, 1200px 1760px, 0 1780px); }
  .band-grey-3 { background: var(--grey); clip-path: polygon(0 2130px, 1200px 2210px, 1200px 2370px, 0 2460px); }

  .band-footer { background: var(--black); clip-path: polygon(0 2440px, 1200px 2360px, 1200px 2860px, 0 2900px); }
  .band-footer-red { background: var(--red); clip-path: polygon(0 2900px, 1200px 2860px, 1200px 3030px, 0 3040px); }

  /* photo areas */
  .photo-garment {
    background: linear-gradient(120deg, #f4f4f2 0%, #e3ebea 45%, #bfe0dc 60%, #eef0ef 100%);
    clip-path: polygon(0 670px, 1200px 560px, 1200px 1000px, 0 940px);
  }
  .photo-workbench {
    background: linear-gradient(90deg, #f1f1f1 0%, #dcdcdc 28%, #e9735a 42%, #e2614a 75%, #d9563f 100%);
    clip-path: polygon(0 1210px, 1200px 1130px, 1200px 1560px, 0 1600px);
  }
  .photo-sketching {
    background: linear-gradient(110deg, #efeae3 0%, #ded4c8 45%, #c9b8a6 75%, #b59d88 100%);
    clip-path: polygon(0 1780px, 1200px 1760px, 1200px 2210px, 0 2130px);
  }

  /* header */
  .brand {
    position: absolute; left: 48px; top: 38px;
    font-size: 84px; font-weight: 700; color: var(--black); letter-spacing: -1px; line-height: 1;
  }

  .headline { position: absolute; left: 0; top: 225px; width: 1200px; text-align: center; line-height: 1; }
  .headline-lead { display: block; font-size: 102px; font-weight: 800; color: var(--white); letter-spacing: 1px; }
  .headline-lead + .headline-lead { margin-top: 8px; }
  .headline-key { display: block; margin-top: 6px; font-size: 178px; font-weight: 900; font-style: italic; color: var(--red); letter-spacing: 2px; }

  /* course blocks */
  .course-title {
    position: absolute; font-weight: 900; font-style: italic; color: var(--red);
    text-transform: uppercase; line-height: 1.05; letter-spacing: 0.5px; white-space: nowrap;
    -webkit-text-stroke: 10px var(--white); paint-order: stroke fill;
  }
  .course-title--short { left: 60px; top: 855px; font-size: 56px; }
  .course-title--advanced { left: 112px; top: 1480px; font-size: 48px; }
  .course-title--diploma { left: 60px; top: 2030px; font-size: 52px; }

  .course-list { position: absolute; list-style: none; font-size: 38px; font-weight: 400; color: var(--ink); line-height: 1.25; white-space: nowrap; }
  .course-list li { position: relative; padding-left: 30px; }
  .course-list li::before { content: "•"; position: absolute; left: 0; }
  .course-list--short { left: 60px; top: 1000px; }
  .course-list--advanced { left: 420px; top: 1625px; font-size: 36px; }
  .course-list--advanced li:nth-child(2) { margin-left: 40px; }
  .course-list--diploma { left: 60px; top: 2180px; font-size: 36px; }

  /* footer */
  .funding { position: absolute; left: 0; top: 2480px; width: 1200px; text-align: center; color: var(--red); line-height: 1; }
  .funding-lead { display: block; font-size: 100px; font-weight: 800; font-style: italic; letter-spacing: 1px; }
  .funding-key { display: block; margin-top: 6px; font-size: 130px; font-weight: 900; font-style: italic; letter-spacing: 2px; }
  .funding-note { position: absolute; left: 100px; top: 2735px; width: 1000px; text-align: center; color: var(--white); font-size: 34px; font-weight: 600; line-height: 1.3; }

  .contact { position: absolute; right: 60px; top: 2900px; text-align: right; font-size: 32px; line-height: 1.3; color: var(--white); font-style: normal; }
  .contact strong { font-weight: 700; }

  .partners { position: absolute; left: 60px; top: 3075px; display: flex; align-items: center; gap: 28px; }
  .badge-centre { width: 210px; height: 84px; border-radius: 42px; background: var(--grey); }
  .badge-seal { width: 88px; height: 88px; border-radius: 50%; background: var(--red); }
</style>
</head>
<body>
<main class="sticker">
  <div class="layer band-top"></div>
  <div class="layer stripe-a"></div>
  <div class="layer stripe-b"></div>

  <div class="layer photo-garment" role="img" aria-label="Stock photo: a light pastel garment laid flat with fashion accessories"></div>
  <div class="layer stripe-red"></div>
  <div class="layer band-grey-1"></div>

  <div class="layer photo-workbench" role="img" aria-label="Stock photo: a sewing machine beside coral fabric on a work table"></div>
  <div class="layer band-grey-2"></div>

  <div class="layer photo-sketching" role="img" aria-label="Stock photo: hands working on design sketches at a desk"></div>
  <div class="layer band-grey-3"></div>

  <div class="layer band-footer"></div>
  <div class="layer band-footer-red"></div>

  <header>
    <div class="brand">BrM.va</div>
  </header>

  <h1 class="headline">
    <span class="headline-lead">STEP INTO</span>
    <span class="headline-lead">THE WORLD OF</span>
    <span class="headline-key">FASHION</span>
  </h1>

  <section class="course">
    <h2 class="course-title course-title--short">Professional KPH<br>Short Courses</h2>
    <ul class="course-list course-list--short">
      <li>Fashion Styling</li>
      <li>Sewing and Alteration</li>
      <li>Leather Care</li>
      <li>Fabric Care</li>
    </ul>
  </section>

  <section class="course">
    <h2 class="course-title course-title--advanced">KPH Advanced Certificate in<br>Fashion Technology</h2>
    <ul class="course-list course-list--advanced">
      <li>Apparel Design &amp; Product Development</li>
      <li>Merchandising and Marketing</li>
    </ul>
  </section>

  <section class="course">
    <h2 class="course-title course-title--diploma">KPH Diploma in<br>Fashion Technology</h2>
    <ul class="course-list course-list--diploma">
      <li>Apparel Design &amp; Product Development</li>
      <li>Merchandising &amp; Marketing</li>
      <li>Footwear Design &amp; Product Development</li>
    </ul>
  </section>

  <footer>
    <h2 class="funding">
      <span class="funding-lead">FUNDING &amp; CAREER</span>
      <span class="funding-key">OPPORTUNITIES</span>
    </h2>
    <p class="funding-note">Speak to us today about your eligibility in funding<br>and potential career opportunities upon graduation.</p>

    <address class="contact">
      Tel: <strong>3824 9057</strong><br>
      Email: <strong>enquiry@brmva-example.org</strong><br>
      Website: <strong>www.brmva-example.edu.sg</strong>
    </address>

    <div class="partners">
      <div class="badge-centre" aria-hidden="true"></div>
      <div class="badge-seal" aria-hidden="true"></div>
    </div>
  </footer>
</main>
</body>
</html>
```